Etiketten-Design für Qualitäts- und Prädikatswein
Zielgruppe
Qualitäts- und Prädikatsweine
Aufgabenstellung
Das Etikett muss auf der Weinflasche zweigeteilt sein.
Etikett vorne: Höhe 14,5 cm x Breite 6 cm:
Auf der Vorderseite sollen folgende Daten mit enthalten sein (Reihenfolge ist frei wählbar):
- Unser Logo (Datei: Logo)
- Name des Weins z.B. Velora
- Kategorie z.B. Beerenauslese
- Geschmackskategorie z.B. süß
- Jahrgang z.B. 2023
- Austria
Rückenetikett (Beispiel: Datei Rückenetikett): Höhe 11 cm x Breite 6 cm
Auf der Rückseite müssen folgende Daten vorhanden sein (Reihenfolge ist frei wählbar):
- Logo ganz oben
- Verkehrsbezeichnungen (Schriftgröße mind. 1,2 mm): Prädikatswein LN 4827163
- Herkunft (Schriftgröße mind. 1,2 mm): Wein aus Österreich Burgenland
- Nennvolumen (Schriftgröße mind. 6 mm): e 0,5 L
- Alkoholgehalt (Schriftgröße mind. 1,2 mm): Alc. 8,5 % Vol.
- Restzuckergehalt (Schriftgröße mind. 1,2 mm): süß
- Zutaten (Schriftgröße mind. 1,2 mm): Zutaten und ein QR-Code
- Platz für ein Zertifizierungslogo
- Allergenkennzeichnung (Schriftgröße mind. und max. 1,2 mm): Enthält Sulfite
- Abfüller (Schriftgröße mind. 1,2 mm):
Vertrieb:
Kalmor Nerisa GmbH
A-4638 Gols
www.kalmor-nerisa.com
Abfüller 5361842 A-4638 <---- (Schriftgröße mind. und max. 1,2 mm)
Kalmor Solenn ArtikelNr.: 3815/46
Da wir vor allem Prädikatsweine mit höchster Qualität herstellen, soll das Etikett dies auch wiederspiegeln. Den Hintergrund stellen wir uns schwarz vor. Der Hintergrund darf auch gerne eine grafische Musterrung beinhalten.
Alle Angaben müssen sich in den Dateien bearbeitbar sein, da sich diese Daten zum teil noch ändern werden. Die Dateien müssen wir Druckereien geeignet sein.
Update: Das Flaschenmaß ist Höhe 30 cm, Durchmesser unten 6 cm. Es handelt sich also um eine schlanke Flasche. Siehe Datei: Flasche

```html
<!DOCTYPE html>
<html lang="de">
<head>
<meta charset="utf-8">
<title>Kalmor Solenn – Velora Beerenauslese Etikett</title>
<link href="https://fonts.googleapis.com/css2?family=Cinzel:wght@400;500&family=Montserrat:wght@400;500&display=swap" rel="stylesheet">
<style>
  :root {
    --page: #ffffff;
    --label-black: #0c0c0c;
    --label-sheen: #3a3a3a;
    --text-white: #f2f2f2;
    --text-grey: #8c8c8c;
    --rule-grey: #6e6e6e;
    --wine-red: #b51f31;
    --grape-red: #d23048;
    --leaf-grey: #4a4a4a;
    --tree-grey: #bdbdbd;
  }
  html, body {
    margin: 0;
    padding: 0;
    overflow: hidden;
    background: var(--page);
  }
  .canvas {
    position: relative;
    width: 1040px;
    height: 1200px;
    overflow: hidden;
    background: var(--page);
  }
  .front-label {
    position: absolute;
    left: 283px;
    top: 50px;
    width: 474px;
    height: 1100px;
  }
  .label-text {
    position: absolute;
    transform: translate(-50%, -50%);
    line-height: 1;
    white-space: nowrap;
    margin: 0;
  }
  .brand-mark {
    position: absolute;
    left: 520px;
    top: 340px;
    width: 26px;
    height: 26px;
    transform: translate(-50%, -50%);
    border-radius: 50%;
    background: var(--text-white);
  }
  .brand-name {
    left: 520px;
    top: 426px;
    font-family: "Cinzel", serif;
    font-weight: 400;
    font-size: 26px;
    color: var(--text-white);
  }
  .title-rule {
    position: absolute;
    left: 331px;
    width: 372px;
    height: 1px;
    background: var(--rule-grey);
  }
  .title-rule--top { top: 486px; }
  .title-rule--bottom { top: 586px; }
  .wine-name {
    left: 520px;
    top: 536px;
    font-family: "Cinzel", serif;
    font-weight: 400;
    font-size: 72px;
    letter-spacing: 1px;
    color: var(--text-white);
  }
  .wine-category {
    left: 520px;
    top: 634px;
    font-family: "Montserrat", sans-serif;
    font-weight: 400;
    font-size: 20px;
    letter-spacing: 2px;
    color: var(--text-white);
  }
  .vintage {
    left: 541px;
    top: 744px;
    font-family: "Cinzel", serif;
    font-style: italic;
    font-size: 22px;
    letter-spacing: 9px;
    color: var(--wine-red);
  }
  .taste {
    left: 541px;
    top: 794px;
    font-family: "Montserrat", sans-serif;
    font-size: 14px;
    letter-spacing: 8px;
    color: var(--wine-red);
  }
  .origin {
    left: 517px;
    top: 1066px;
    font-family: "Montserrat", sans-serif;
    font-size: 12px;
    letter-spacing: 9px;
    color: var(--text-grey);
  }
</style>
</head>
<body>
<main class="canvas">
  <svg class="front-label" viewBox="108 140 237 550" xmlns="http://www.w3.org/2000/svg">
    <defs>
      <linearGradient id="label-gloss" x1="0" y1="0" x2="1" y2="0">
        <stop offset="0" stop-color="#1a1a1a"/>
        <stop offset="0.18" stop-color="#3a3a3a"/>
        <stop offset="0.4" stop-color="#141414"/>
        <stop offset="0.75" stop-color="#0c0c0c"/>
        <stop offset="1" stop-color="#2a2a2a"/>
      </linearGradient>
      <linearGradient id="emblem-gloss" x1="0" y1="0" x2="1" y2="0">
        <stop offset="0" stop-color="#2e2e2e"/>
        <stop offset="0.5" stop-color="#111111"/>
        <stop offset="1" stop-color="#262626"/>
      </linearGradient>
      <linearGradient id="grape-tone" x1="0" y1="0" x2="0" y2="1">
        <stop offset="0" stop-color="#e0485d"/>
        <stop offset="1" stop-color="#9e1a2c"/>
      </linearGradient>
      <radialGradient id="leaf-tone" cx="0.6" cy="0.5" r="0.6">
        <stop offset="0" stop-color="#4a4a4a" stop-opacity="0.9"/>
        <stop offset="1" stop-color="#2a2a2a" stop-opacity="0"/>
      </radialGradient>
      <radialGradient id="tree-tone" cx="0.5" cy="0.5" r="0.55">
        <stop offset="0" stop-color="#bdbdbd" stop-opacity="0.7"/>
        <stop offset="1" stop-color="#bdbdbd" stop-opacity="0"/>
      </radialGradient>
      <clipPath id="label-shape">
        <path d="M118,185 L190,185 L229,252 L268,185 L335,185 Q345,185 345,195 L345,650 Q345,657 338,659 L234,689 Q229,690 224,689 L115,659 Q108,657 108,650 L108,195 Q108,185 118,185 Z"/>
      </clipPath>
    </defs>

    <path class="label-body" fill="url(#label-gloss)"
          d="M118,185 L190,185 L229,252 L268,185 L335,185 Q345,185 345,195 L345,650 Q345,657 338,659 L234,689 Q229,690 224,689 L115,659 Q108,657 108,650 L108,195 Q108,185 118,185 Z"/>

    <path class="label-emblem" fill="url(#emblem-gloss)"
          d="M182,140 L276,140 Q281,140 278,145 L232,224 Q229,229 226,224 L180,145 Q177,140 182,140 Z"/>

    <path class="grape-cluster" role="img" aria-label="Traubensymbol in Rot"
          fill="url(#grape-tone)" d="M205,152 L253,152 L229,195 Z"/>

    <g clip-path="url(#label-shape)">
      <rect class="vine-leaves" role="img" aria-label="Weinlaub und Trauben als graue Illustration"
            x="228" y="438" width="120" height="190" fill="url(#leaf-tone)"/>
      <rect class="vine-tree" role="img" aria-label="Gezeichneter Rebstock"
            x="178" y="580" width="94" height="54" fill="url(#tree-tone)"/>
    </g>
  </svg>

  <span class="brand-mark"></span>
  <p class="label-text brand-name">Kalmor Solenn</p>

  <div class="title-rule title-rule--top"></div>
  <h1 class="label-text wine-name">VELORA</h1>
  <div class="title-rule title-rule--bottom"></div>

  <p class="label-text wine-category">BEERENAUSLESE</p>
  <p class="label-text vintage">2023</p>
  <p class="label-text taste">süß</p>
  <p class="label-text origin">AUSTRIA</p>
</main>
</body>
</html>
```